Square Business Cards for Our Restaurant / Event Venue

We need square business cards designed for the management team of our event venue and restaurant. On one side of the card should be the the Harbor Lantern 7 logo and URL www.harborlantern7.example. On the other side should be the Ember Logo and URL www.emberhall7.example. All employee details should be on the side with Ember logo. There will be a total of 5 cards to be created with the design.

Clara Bennquist
clara@harborlantern7.example

main 555.418.3072
direct 555.730.2946

4831 West Orchard Lane SE
Washington, DC 90417

Industry/Entity Type

Business

```html
<!DOCTYPE html>
<html lang="en">
<head>
<meta charset="utf-8">
<title>Harbor Lantern 7 · Ember — Square Business Card</title>
<link rel="stylesheet" href="https://fonts.googleapis.com/css2?family=Montserrat:wght@400;500;600&family=Josefin+Sans:wght@300;400&display=swap">
<style>
  :root {
    --backdrop: #999999;
    --brand-red: #9c2823;
    --card-white: #fafafa;
    --ink: #1a1a1a;
    --paper: #ffffff;
  }
  * { margin: 0; padding: 0; box-sizing: border-box; }
  html, body {
    width: 1200px;
    height: 759px;
    overflow: hidden;
    background: var(--backdrop);
  }
  .sheet {
    position: relative;
    width: 1200px;
    height: 759px;
  }
  .card {
    position: absolute;
    top: 195px;
    width: 370px;
    height: 370px;
    overflow: hidden;
  }

  /* Front side */
  .card--front {
    left: 188px;
    background: var(--brand-red);
  }
  .front-badge {
    position: absolute;
    left: 73px;
    top: 50px;
    width: 224px;
    height: 224px;
    border-radius: 50%;
    background: var(--paper);
    display: flex;
    align-items: center;
    justify-content: center;
    text-align: center;
  }
  .front-badge__name {
    font-family: "Josefin Sans", sans-serif;
    font-weight: 400;
    font-size: 27px;
    line-height: 1.2;
    color: var(--brand-red);
    width: 170px;
  }
  .front-url {
    position: absolute;
    left: 0;
    right: 0;
    top: 329px;
    text-align: center;
    font-family: "Montserrat", sans-serif;
    font-weight: 400;
    font-size: 14px;
    color: var(--paper);
    letter-spacing: 0.1px;
  }

  /* Back side */
  .card--back {
    left: 641px;
    background: var(--card-white);
  }
  .back-brand {
    position: absolute;
    left: 0;
    right: 0;
    top: 62px;
    text-align: center;
    font-family: "Montserrat", sans-serif;
    font-weight: 600;
    font-size: 64px;
    line-height: 1;
    color: var(--ink);
  }
  .contact {
    position: absolute;
    left: 0;
    right: 0;
    top: 188px;
    text-align: center;
    font-family: "Montserrat", sans-serif;
  }
  .contact__name {
    font-weight: 500;
    font-size: 27px;
    line-height: 30px;
    color: var(--brand-red);
    margin-bottom: 5px;
  }
  .contact__lines {
    list-style: none;
    font-weight: 400;
    font-size: 15.5px;
    line-height: 19.2px;
    color: var(--ink);
  }
  .accent { color: var(--brand-red); }
  .back-band {
    position: absolute;
    left: 0;
    right: 0;
    bottom: 0;
    height: 10px;
    background: var(--brand-red);
  }
</style>
</head>
<body>
  <main class="sheet">
    <section class="card card--front" aria-label="Card front">
      <div class="front-badge">
        <span class="front-badge__name">Harbor Lantern 7</span>
      </div>
      <p class="front-url">www.harborlantern7.example</p>
    </section>

    <section class="card card--back" aria-label="Card back">
      <p class="back-brand">Ember</p>
      <div class="contact">
        <h1 class="contact__name">Clara Bennquist</h1>
        <ul class="contact__lines">
          <li>555.418.3072</li>
          <li>555.730.2946</li>
          <li>www.<span class="accent">emberhall7</span>.example</li>
          <li>clara@<span class="accent">harborlantern7</span>.example</li>
          <li>4831 West Orchard Lane SE</li>
          <li>Washington, DC 90417</li>
        </ul>
      </div>
      <div class="back-band"></div>
    </section>
  </main>
</body>
</html>
```